Graphic Design Project-Label for New Bourbon

Hi Designers

This is a new label for a Bourbon .Im looking for a smart looking label, Mordern,Simple .Clean.

Bottle type is the same as Harlow Gin Bottle if you google or can use others bottles glass.

I am open to new bourbon names and would love to see your creativity.

The Label Name is currently called Copper Ridge
Size is 1 litre.
Percentage is 37.5%.
Updates

Target Market(s)

ALL bourbon drinkers

Industry/Entity Type

Graphic Design

Requirements
Must have
• Up on top chosen label will send ingrediance final changes

```html
<!DOCTYPE html>
<html lang="en">
<head>
<meta charset="utf-8">
<title>Copper Ridge Bourbon Whiskey Label</title>
<link rel="stylesheet" href="https://fonts.googleapis.com/css2?family=Barlow+Condensed:wght@500;600;700&family=Barlow+Semi+Condensed:wght@700;800&display=swap">
<style>
  :root {
    --kraft: #e2d6ba;
    --kraft-shade: #d6c8a7;
    --ink: #231f1c;
    --red: #cd1f27;
  }
  * { margin: 0; padding: 0; box-sizing: border-box; }
  html, body { width: 831px; height: 1200px; overflow: hidden; background: var(--kraft); }
  .label {
    position: relative;
    width: 831px;
    height: 1200px;
    overflow: hidden;
    background: radial-gradient(ellipse at 50% 45%, #e6dbc1 0%, var(--kraft) 60%, var(--kraft-shade) 100%);
    color: var(--ink);
    font-family: "Barlow Condensed", "Arial Narrow", sans-serif;
  }
  .age-statement {
    position: absolute;
    left: 124px;
    top: 130px;
    font-weight: 700;
    font-size: 27px;
    letter-spacing: 0.2px;
    color: var(--red);
    white-space: nowrap;
  }
  .brand-name {
    position: absolute;
    font-family: "Barlow Semi Condensed", "Arial Narrow", sans-serif;
    font-weight: 800;
    line-height: 1;
    white-space: nowrap;
    color: var(--ink);
  }
  .brand-name--first {
    left: -10px;
    top: 168px;
    font-size: 176px;
    letter-spacing: -2px;
  }
  .brand-name--second {
    left: 118px;
    top: 318px;
    font-size: 350px;
    letter-spacing: -6px;
  }
  .style-band {
    position: absolute;
    left: 0;
    top: 762px;
    width: 831px;
    height: 108px;
  }
  .emblem {
    position: absolute;
    left: 124px;
    top: 748px;
    width: 132px;
    height: 132px;
  }
  .style-name {
    position: absolute;
    left: 292px;
    top: 786px;
    font-weight: 700;
    font-size: 62px;
    letter-spacing: 1px;
    line-height: 1;
    color: var(--ink);
    white-space: nowrap;
  }
  .facts {
    position: absolute;
    left: 124px;
    top: 1027px;
    height: 88px;
    display: flex;
    align-items: stretch;
  }
  .fact {
    display: flex;
    flex-direction: column;
    justify-content: center;
    padding: 0 16px;
    border-left: 3px solid var(--red);
  }
  .fact:first-child { padding-left: 0; border-left: none; }
  .fact__value {
    font-weight: 700;
    font-size: 56px;
    line-height: 0.95;
    white-space: nowrap;
  }
  .fact__value sup {
    font-size: 26px;
    vertical-align: top;
    position: relative;
    top: 2px;
    margin-left: 2px;
  }
  .fact__unit {
    font-weight: 600;
    font-size: 18px;
    letter-spacing: 0.5px;
    margin-top: 4px;
    white-space: nowrap;
  }
  .producer__intro {
    font-weight: 600;
    font-size: 21px;
    white-space: nowrap;
  }
  .producer__name {
    font-weight: 700;
    font-size: 32px;
    margin-top: 10px;
    letter-spacing: 0.5px;
    white-space: nowrap;
  }
</style>
</head>
<body>
<main class="label">
  <p class="age-statement">AGED UNDER 4 YEARS IN AMERICAN OAK</p>
  <h1 class="brand-name brand-name--first">COPPER</h1>
  <p class="brand-name brand-name--second">RIDGE</p>

  <svg class="style-band" viewBox="0 0 831 108" aria-hidden="true">
    <defs>
      <pattern id="teeth-top" width="10" height="8" patternUnits="userSpaceOnUse">
        <polygon points="0,8 5,0 10,8" fill="#cd1f27"/>
      </pattern>
      <pattern id="teeth-bottom" width="10" height="8" patternUnits="userSpaceOnUse">
        <polygon points="0,0 5,8 10,0" fill="#cd1f27"/>
      </pattern>
    </defs>
    <rect x="0" y="0" width="831" height="8" fill="url(#teeth-top)"/>
    <rect x="0" y="8" width="831" height="92" fill="#cd1f27"/>
    <rect x="0" y="100" width="831" height="8" fill="url(#teeth-bottom)"/>
  </svg>

  <svg class="emblem" viewBox="0 0 132 132" aria-hidden="true">
    <circle cx="66" cy="66" r="58" fill="#e2d6ba" stroke="#231f1c" stroke-width="12"/>
  </svg>

  <p class="style-name">BOURBON WHISKEY</p>

  <section class="facts">
    <div class="fact">
      <span class="fact__value">37.5<sup>%</sup></span>
      <span class="fact__unit">ALC BY VOL</span>
    </div>
    <div class="fact">
      <span class="fact__value">1000<sup>ml</sup></span>
      <span class="fact__unit">33.8 FL. OZ.</span>
    </div>
    <div class="fact producer">
      <span class="producer__intro">Distilled &amp; Bottled by</span>
      <span class="producer__name">RIDGELINE DISTILLERY</span>
    </div>
  </section>
</main>
</body>
</html>
```